Cobalt MesaLighting and Design Web Page

We are a Sales Agency that represents 40+ LED Lighting manufacturers primarily in new commercial, industrial and architectural construction projects. We also are active in the Re-Light and Retrofit Lighting market.
Our current web page can be found at www.cobaltmesalighting.example. Our local competitors are www.brightfieldlampsnw.example,. We would like a more dynamic website that will list our manufacturers we represent and links to their websites. Please offer suggestions to provide a more dynamic website using our new logo which is attached. Please use the color scheme from logo. The final design should communicate innovation and expertise in LED lighting.

Target Market(s)

Architects, Lighting designers, Electrical Engineers, Electrical Contractors, Electrical Distributors, Facility Engineers, Energy Engineers

Industry/Entity Type

Construction

Number of Pages Required

5+ page

Font styles to use
Other font styles liked:
• MS Reference Sans Serif, or close to our LOGO font.

Colors
f78f20
959595

Requirements
Must have
• Logo incorporated with matching background, clean professional look based on logo, links to our manufacturers web page
Nice to have
• LED Lighting project stock photos as examples
Should not have
• crowded pages with text

```html
<!DOCTYPE html>
<html lang="en">
<head>
<meta charset="utf-8">
<title>Cobalt Mesa Lighting</title>
<link rel="stylesheet" href="https://fonts.googleapis.com/css2?family=Michroma&family=Lato:wght@400;700&display=swap">
<style>
:root{
  --orange:#e8590c;
  --orange-soft:#f78f20;
  --gray:#959595;
  --nav:#5b5b5b;
  --ink:#333;
  --text:#555;
  --dark:#141414;
  --footer:#262626;
  --light:#e6e6e6;
  --white:#fff;
}
*{box-sizing:border-box;margin:0;padding:0}
html,body{width:1200px;height:2848px;overflow:hidden}
body{font-family:"Lato",sans-serif;color:var(--text);background:var(--white);position:relative}
.wide{font-family:"Michroma",sans-serif}
.container{width:1040px;margin:0 auto;position:relative}

/* header */
.site-header{height:118px;display:flex;align-items:center}
.site-header .container{display:flex;justify-content:space-between;align-items:center}
.brand{display:flex;align-items:center;gap:14px}
.brand-dot{width:58px;height:58px;border-radius:50%;background:var(--orange)}
.brand-name{font-family:"Lato",sans-serif;font-weight:700;font-size:22px;color:var(--ink);line-height:1.1;width:150px}
.contact-bar{display:flex;gap:46px}
.contact-item{display:flex;align-items:center;gap:14px}
.contact-icon{width:46px;height:46px}
.contact-label{font-family:"Michroma",sans-serif;color:var(--orange);font-size:15px}
.contact-value{font-size:15px;color:var(--ink)}

/* nav */
.main-nav{height:49px;background:var(--nav)}
.main-nav ul{list-style:none;display:flex;height:49px;align-items:center;width:1040px;margin:0 auto}
.main-nav li{font-family:"Michroma",sans-serif;color:var(--white);font-size:13px;padding:0 20px;height:49px;display:flex;align-items:center;position:relative}
.main-nav li+li::before{content:"";position:absolute;left:0;top:20px;height:10px;border-left:1px solid #888}
.main-nav li.active{background:var(--orange);padding:0 22px}

/* hero */
.hero{height:509px;position:relative;background:linear-gradient(180deg,#6e5b4a 0%,#b7a38c 38%,#8b7560 70%,#4c3c30 100%)}
.hero-caption{position:absolute;left:0;right:0;bottom:30px;text-align:center;color:var(--white);font-weight:700;font-size:29px;line-height:1.2;text-shadow:0 2px 4px rgba(0,0,0,.6)}
.slider-arrow{position:absolute;top:230px;width:40px;height:40px;border-radius:50%;background:var(--white);display:flex;align-items:center;justify-content:center}
.slider-arrow.prev{left:32px}.slider-arrow.next{right:32px}

/* section headings */
.section-title{font-family:"Michroma",sans-serif;font-size:27px;text-align:center;color:var(--ink);letter-spacing:1px}
.section-title span{color:var(--orange)}
.title-rule{width:80px;border-top:2px solid var(--orange);margin:22px auto 0}

/* button */
.pill{position:relative;display:inline-block;background:#5d5d5d;color:var(--white);font-family:"Michroma",sans-serif;font-size:15px;padding:12px 30px;border-radius:22px}
.pill::before{content:"";position:absolute;left:-8px;top:-8px;width:52px;height:58px;border-radius:50%;border:3px solid var(--orange);border-color:var(--orange) transparent transparent var(--orange);transform:rotate(-20deg)}

/* welcome */
.welcome{height:350px;padding-top:38px;text-align:center}
.welcome .lead{margin-top:34px;font-weight:700;font-size:13.5px;color:var(--ink)}
.welcome p{font-size:13.5px;line-height:1.6;margin-top:10px;padding:0 10px}
.welcome .pill{margin-top:30px}

/* services */
.services{height:484px;background:radial-gradient(ellipse at 50% 40%,#2d2d2d 0%,var(--dark) 75%);padding-top:40px}
.services .section-title{color:var(--white)}
.service-grid{display:flex;justify-content:space-between;margin-top:48px}
.service-card{width:240px;text-align:center;color:var(--white)}
.service-photo{height:160px;border:3px solid var(--white)}
.service-card h3{font-size:19px;font-weight:700;margin-top:16px}
.service-card p{font-size:13px;color:#ccc;line-height:1.45;margin-top:6px}
.plus{width:24px;height:24px;border-radius:50%;background:var(--orange);margin:12px auto 0;display:flex;align-items:center;justify-content:center}

/* blog */
.blog{height:488px;padding-top:38px}
.blog-grid{display:flex;justify-content:space-between;margin-top:50px}
.blog-post{width:490px;display:flex;gap:24px}
.blog-photo{width:209px;height:209px;flex:none;border:2px solid #ccc}
.blog-post h4{color:var(--orange);font-size:16px;font-weight:700}
.meta{display:flex;gap:22px;font-size:13px;color:var(--ink);margin-top:10px;align-items:center}
.meta span{display:flex;gap:6px;align-items:center}
.blog-post p{font-size:13px;line-height:1.75;color:var(--ink);margin-top:12px}
.read-more{display:inline-block;margin-top:10px;font-size:13px;font-weight:700;color:var(--ink);text-decoration:underline}
.blog .center{text-align:center;margin-top:38px}

/* gallery */
.gallery-head{height:125px;background:var(--light);padding-top:38px}
.gallery-strip{height:228px;display:flex}
.gallery-tile{width:300px;height:228px;position:relative}
.gallery-overlay{position:absolute;left:14px;top:10px;width:300px;height:200px;background:rgba(40,32,26,.85);text-align:center;padding:24px 26px;color:var(--white)}
.gallery-overlay h5{font-family:"Michroma",sans-serif;color:var(--orange);font-size:15px;font-weight:400}
.gallery-overlay p{font-size:12.5px;line-height:1.4;margin-top:10px}
.gallery-nav{height:99px;background:var(--light);position:relative}
.gallery-nav::before{content:"";position:absolute;left:0;right:0;top:47px;border-top:2px solid #bbb}
.gallery-dots{position:absolute;left:578px;top:33px;display:flex;gap:6px}
.gallery-dots span{width:28px;height:28px;border-radius:50%;display:flex;align-items:center;justify-content:center}

/* footer */
.site-footer{height:347px;background:var(--footer);color:#ddd;padding-top:50px}
.footer-grid{display:flex}
.footer-col h6{font-family:"Michroma",sans-serif;font-size:14px;font-weight:400;color:var(--white);letter-spacing:.5px}
.footer-col .rule{width:40px;border-top:2px solid var(--gray);margin:12px 0 16px}
.quick-links{width:195px;border-right:1px solid #3a3a3a}
.quick-links li{list-style:none;font-size:13px;line-height:25px}
.contact-details{width:307px;padding-left:0;border-right:1px solid #3a3a3a}
.contact-col{padding-left:0}
.detail{display:flex;gap:12px;font-size:13px;line-height:1.55;margin-bottom:12px}
.detail svg{flex:none;margin-top:2px}
.inquiry{width:302px;border-right:1px solid #3a3a3a;padding-right:30px}
.field{background:#1b1b1b;border:1px solid #444;font-size:13px;color:var(--white);font-weight:700;padding:8px 10px;margin-bottom:8px}
.field.tall{height:64px}
.submit{display:inline-block;background:var(--orange);color:var(--white);font-size:12px;font-weight:700;padding:7px 20px;border-radius:14px;margin-top:4px}
.footer-brand{flex:1;display:flex;flex-direction:column;align-items:center;padding-top:40px}
.footer-brand .brand-name{color:#ccc;font-size:21px}
.socials{display:flex;gap:10px;margin-top:16px}
.socials span{width:28px;height:28px;border-radius:50%;background:#1d6fb8;border:2px solid var(--white)}
.copyright{height:51px;background:var(--orange);color:var(--white);font-size:13px;text-align:center;line-height:51px}
</style>
</head>
<body>

<header class="site-header">
  <div class="container">
    <div class="brand"><span class="brand-dot"></span><span class="brand-name">Cobalt Mesa Lighting</span></div>
    <div class="contact-bar">
      <div class="contact-item">
        <svg class="contact-icon" viewBox="0 0 46 46"><path d="M8 30 A18 18 0 0 1 30 6" fill="none" stroke="#e8590c" stroke-width="3"/><path d="M18 14c2 0 3 4 2 5l-2 2c1 3 4 6 7 7l2-2c1-1 5 0 5 2l0 3c0 1-1 2-3 2-9 0-16-7-16-16 0-2 1-3 2-3z" fill="#e8590c"/></svg>
        <div><div class="contact-label">CALL US:</div><div class="contact-value">505-555-0142</div></div>
      </div>
      <div class="contact-item">
        <svg class="contact-icon" viewBox="0 0 46 46"><path d="M8 30 A18 18 0 0 1 30 6" fill="none" stroke="#e8590c" stroke-width="3"/><rect x="13" y="16" width="22" height="15" fill="#e8590c"/><path d="M13 16l11 9 11-9" fill="none" stroke="#fff" stroke-width="2"/></svg>
        <div><div class="contact-label">MAIL US:</div><div class="contact-value">sales@cobaltmesalighting.example</div></div>
      </div>
    </div>
  </div>
</header>

<nav class="main-nav">
  <ul>
    <li class="active">HOME</li><li>ABOUT</li><li>LINE CARD</li><li>SERVICES</li><li>TERRITORY MAP</li><li>PHOTO GALLERY</li><li>BLOG</li><li>CONTACT</li>
  </ul>
</nav>

<section class="hero" role="img" aria-label="Warmly lit hotel bedroom with recessed LED ceiling lighting">
  <div class="slider-arrow prev"><svg width="14" height="14" viewBox="0 0 14 14"><path d="M9 2L4 7l5 5" fill="none" stroke="#333" stroke-width="2"/></svg></div>
  <div class="slider-arrow next"><svg width="14" height="14" viewBox="0 0 14 14"><path d="M5 2l5 5-5 5" fill="none" stroke="#333" stroke-width="2"/></svg></div>
  <div class="hero-caption">Exceed Customer And Manufacturer Expectations By Providing High-quality<br>Technical Support And The Best In Class Customer Service</div>
</section>

<section class="welcome">
  <div class="container">
    <h2 class="section-title">WELCOME TO <span>COBALT MESA LIGHTING</span></h2>
    <div class="title-rule"></div>
    <p class="lead">Cobalt Mesa Lighting was established in 1996 and is the leading lighting and controls agency in the region servicing West Texas, New Mexico, and Mexico (Country).</p>
    <p>We are a team of experienced and talented individuals who share the same passion: "Exceed customer and manufacturer expectations by providing high-quality technical support and the best in class customer service", experts in LED Lighting systems for architectural, commercial, industrial, institutional, and residential purposes as well as controls projects.</p>
    <span class="pill">READ MORE</span>
  </div>
</section>

<section class="services">
  <div class="container">
    <h2 class="section-title">OUR <span>SERVICES</span></h2>
    <div class="title-rule"></div>
    <div class="service-grid">
      <div class="service-card">
        <div class="service-photo" role="img" aria-label="Hands sketching lighting plans on paper" style="background:linear-gradient(135deg,#d9d3c8,#b59a78)"></div>
        <h3>Design Assistance</h3><p>Cobalt Mesa Lighting offers interior<br>and exterior lighting design...</p>
        <div class="plus"><svg width="10" height="10"><path d="M5 1v8M1 5h8" stroke="#fff" stroke-width="2"/></svg></div>
      </div>
      <div class="service-card">
        <div class="service-photo" role="img" aria-label="Audience attending a training seminar" style="background:linear-gradient(135deg,#e4e2de,#8a7a6a)"></div>
        <h3>Training</h3><p>Cobalt Mesa Lighting offers training to<br>all stakeholders plus coordinated...</p>
        <div class="plus"><svg width="10" height="10"><path d="M5 1v8M1 5h8" stroke="#fff" stroke-width="2"/></svg></div>
      </div>
      <div class="service-card">
        <div class="service-photo" role="img" aria-label="Team planning a project around a table with documents" style="background:linear-gradient(135deg,#a87b57,#6f7b8a)"></div>
        <h3>Project Management</h3><p>Cobalt Mesa Lighting offers complete<br>project management of...</p>
        <div class="plus"><svg width="10" height="10"><path d="M5 1v8M1 5h8" stroke="#fff" stroke-width="2"/></svg></div>
      </div>
      <div class="service-card">
        <div class="service-photo" role="img" aria-label="Light bulb with a growing plant held in a hand" style="background:linear-gradient(180deg,#dfe7c0,#8fae45)"></div>
        <h3>Energy Saving Projects</h3><p>Cobalt Mesa Lighting offers a<br>complete set of solutions for...</p>
        <div class="plus"><svg width="10" height="10"><path d="M5 1v8M1 5h8" stroke="#fff" stroke-width="2"/></svg></div>
      </div>
    </div>
  </div>
</section>

<section class="blog">
  <div class="container">
    <h2 class="section-title">LATEST <span>BLOG POSTS</span></h2>
    <div class="title-rule"></div>
    <div class="blog-grid">
      <article class="blog-post">
        <div class="blog-photo" role="img" aria-label="Storefront lit with blue LED strips at night" style="background:linear-gradient(135deg,#0b2b6a,#1f8fd6 60%,#c58a3a)"></div>
        <div>
          <h4>Lorem ipsum dolor laoreet met...</h4>
          <div class="meta"><span><svg width="12" height="12"><rect x="1" y="2" width="10" height="9" fill="none" stroke="#333" stroke-width="1.5"/><path d="M1 5h10" stroke="#333"/></svg>25 May</span><span><svg width="12" height="12"><circle cx="6" cy="4" r="3" fill="#333"/><path d="M1 12a5 4 0 0 1 10 0z" fill="#333"/></svg>Admin</span></div>
          <p>Lorem ipsum dolor sit aconsectetuer adip iscing elit, sediam nonummy nibh euismod tincidunt ut laoreet dolore magna aliquam erat volutpat. Ut wisi enim adedianonummy nibh euismod tinliq min nostrud .</p>
          <span class="read-more">Read More →</span>
        </div>
      </article>
      <article class="blog-post">
        <div class="blog-photo" role="img" aria-label="Bright dining room with round table and pendant light" style="background:linear-gradient(135deg,#efe7d8,#c9b38e)"></div>
        <div>
          <h4>Lorem ipsum dolor laoreet met...</h4>
          <div class="meta"><span><svg width="12" height="12"><rect x="1" y="2" width="10" height="9" fill="none" stroke="#333" stroke-width="1.5"/><path d="M1 5h10" stroke="#333"/></svg>25 May</span><span><svg width="12" height="12"><circle cx="6" cy="4" r="3" fill="#333"/><path d="M1 12a5 4 0 0 1 10 0z" fill="#333"/></svg>Admin</span></div>
          <p>Lorem ipsum dolor sit aconsectetuer adip iscing elit, sediam nonummy nibh euismod tincidunt ut laoreet dolore magna aliquam erat volutpat. Ut wisi enim adedianonummy nibh euismod tinliq min nostrud .</p>
          <span class="read-more">Read More →</span>
        </div>
      </article>
    </div>
    <div class="center"><span class="pill">VIEW ALL</span></div>
  </div>
</section>

<section class="gallery">
  <div class="gallery-head">
    <h2 class="section-title">PHOTO <span>GALLERY</span></h2>
    <div class="title-rule"></div>
  </div>
  <div class="gallery-strip">
    <div class="gallery-tile" role="img" aria-label="Building facade washed in green and blue LED light at night" style="background:linear-gradient(135deg,#0d2a52,#3fae5a 55%,#0b1a33)"></div>
    <div class="gallery-tile" role="img" aria-label="Atrium interior with skylight and balconies" style="background:linear-gradient(180deg,#8fb4d6,#e2d8c6 60%,#9a8464)"></div>
    <div class="gallery-tile" style="background:linear-gradient(180deg,#b86a2c,#5a3520)" role="img" aria-label="Warm lit interior project">
      <div class="gallery-overlay">
        <h5>LOREM IPSUM</h5>
        <p>Lorem ipsum dolor sit amet, consectetuer adipiscing elit, sed diam nonummy nibh euismod tincidunt ut laoreet dolore magna aliquam erat volutpat. Ut wisi enim</p>
        <div class="plus"><svg width="10" height="10"><path d="M5 1v8M1 5h8" stroke="#fff" stroke-width="2"/></svg></div>
      </div>
    </div>
    <div class="gallery-tile" role="img" aria-label="Industrial warehouse with rows of high bay LED fixtures" style="background:linear-gradient(180deg,#2a3442,#6e7a86 60%,#a3865a)"></div>
  </div>
  <div class="gallery-nav">
    <div class="gallery-dots">
      <span style="background:#666"><svg width="10" height="10"><path d="M7 1L3 5l4 4" fill="none" stroke="#fff" stroke-width="2"/></svg></span>
      <span style="background:var(--orange)"><svg width="10" height="10"><path d="M3 1l4 4-4 4" fill="none" stroke="#fff" stroke-width="2"/></svg></span>
    </div>
  </div>
</section>

<footer class="site-footer">
  <div class="container footer-grid">
    <div class="footer-col quick-links">
      <h6>QUICK LINKS</h6><div class="rule"></div>
      <ul><li>• Home</li><li>• About</li><li>• Line Card</li><li>• Services</li><li>• Territory Map</li><li>• Photo Gallery</li><li>• Blog</li><li>• Contact</li></ul>
    </div>
    <div class="footer-col contact-details" style="padding-left:0;margin-left:0">
      <h6>CONTACT DETAILS</h6><div class="rule"></div>
      <div class="detail"><svg width="14" height="16"><path d="M7 1a5 5 0 0 1 5 5c0 4-5 9-5 9S2 10 2 6a5 5 0 0 1 5-5z" fill="#ddd"/><circle cx="7" cy="6" r="2" fill="#262626"/></svg><div><b>Cobalt Mesa Lighting</b><br>4410 Larkspur Avenue<br>Sun Ridge, TX 79000</div></div>
      <div class="detail"><svg width="14" height="14"><path d="M3 1c2 0 2 3 1 4 1 2 3 4 5 5 1-1 4-1 4 1l0 2c-8 0-12-4-12-12z" fill="#ddd"/></svg>505-555-0142</div>
      <div class="detail"><svg width="14" height="12"><rect x="1" y="2" width="12" height="9" fill="#ddd"/><path d="M1 2l6 5 6-5" fill="none" stroke="#262626"/></svg>sales@cobaltmesalighting.example</div>
      <div class="detail"><svg width="14" height="12"><rect x="1" y="2" width="12" height="9" fill="#ddd"/><path d="M1 2l6 5 6-5" fill="none" stroke="#262626"/></svg>ventas@cobaltmesalighting.example</div>
      <div class="detail"><svg width="14" height="12"><rect x="1" y="2" width="12" height="9" fill="#ddd"/><path d="M1 2l6 5 6-5" fill="none" stroke="#262626"/></svg>applications@cobaltmesalighting.example</div>
    </div>
    <div class="footer-col inquiry" style="padding-left:0">
      <h6>QUICK &nbsp;INQUIRY</h6><div class="rule"></div>
      <div class="field">Name</div>
      <div class="field">Email</div>
      <div class="field tall">Message</div>
      <span class="submit">SUBMIT</span>
    </div>
    <div class="footer-brand">
      <div class="brand"><span class="brand-dot" style="background:#555"></span><span class="brand-name">Cobalt Mesa Lighting</span></div>
      <div class="socials"><span></span><span></span><span></span></div>
    </div>
  </div>
</footer>
<div class="copyright">Copyright © 2017 COBALT MESA LIGHTING. All Right Reserved</div>

</body>
</html>
```